Business Card for: Northbrook Financial Advisory Services Inc.

provide strategic financial advisory services to companies in the areas of corporate finance, mergers and acquisitions, executive coaching and strategic planning

Target Market(s)

Companies, banks, accountants, lawyers

Industry/Entity Type

High end business consulting in corporate finance, mergers and acquisitions, consulting

Contact Information for Business Card

Name of company, Name: xxxxxx xxxxxx , CEO, - phone number: 1-xxx-xxx-xxxx, - email address,

Requirements
Must have
• Must be professional and simple.
Nice to have
• simple, straight graphics, must give the impression that we are trustworthy, professional, competent
Should not have
• loud colors, loud design features

```html
<!DOCTYPE html>
<html lang="en">
<head>
<meta charset="utf-8">
<title>Northbrook Financial Inc. — Business Card</title>
<link href="https://fonts.googleapis.com/css2?family=Inter:wght@400;500;600;700&display=swap" rel="stylesheet">
<style>
  :root {
    --navy: #14365a;
    --navy-deep: #102d4c;
    --ink: #1e1e1e;
    --text-grey: #444444;
    --title-slate: #5a6287;
    --rule: #555555;
    --band-grey: #636363;
    --paper: #ffffff;
    --backdrop: #e6e6e6;
  }
  * { margin: 0; padding: 0; box-sizing: border-box; }
  html, body {
    width: 1200px;
    height: 1200px;
    overflow: hidden;
    background: var(--backdrop);
    font-family: "Inter", sans-serif;
  }
  .card {
    position: absolute;
    left: 179px;
    width: 861px;
    height: 496px;
    overflow: hidden;
  }
  .card-front {
    top: 84px;
    background: radial-gradient(ellipse at 50% 60%, var(--navy) 0%, var(--navy) 55%, var(--navy-deep) 100%);
  }
  .front-name {
    position: absolute;
    left: 0; right: 0;
    top: 300px;
    text-align: center;
    color: var(--paper);
    font-weight: 600;
    font-size: 45px;
    line-height: 1;
    letter-spacing: -0.2px;
  }
  .card-back {
    top: 622px;
    height: 494px;
    background: var(--paper);
  }
  .back-company {
    position: absolute;
    left: 34px;
    top: 44px;
    color: var(--ink);
    font-weight: 700;
    font-size: 49px;
    line-height: 1;
    letter-spacing: -0.5px;
  }
  .back-company .dot { color: var(--navy); }
  .person-name {
    position: absolute;
    left: 32px;
    top: 234px;
    color: var(--ink);
    font-weight: 600;
    font-size: 42px;
    line-height: 1;
    letter-spacing: 1px;
  }
  .person-title {
    position: absolute;
    left: 32px;
    top: 280px;
    color: var(--title-slate);
    font-weight: 500;
    font-size: 30px;
    line-height: 1;
    letter-spacing: 0.5px;
  }
  .divider {
    position: absolute;
    left: 31px;
    top: 314px;
    width: 759px;
    height: 1px;
    background: var(--rule);
  }
  .contact-list {
    position: absolute;
    left: 32px;
    top: 338px;
    list-style: none;
  }
  .contact-item {
    display: flex;
    align-items: center;
    height: 38.5px;
    color: var(--text-grey);
    font-size: 26px;
    letter-spacing: 4px;
  }
  .contact-icon {
    width: 30px;
    height: 30px;
    margin-right: 12px;
    flex: none;
    fill: var(--navy);
  }
  .address {
    position: absolute;
    right: 71px;
    top: 338px;
    text-align: right;
    color: var(--text-grey);
    font-size: 26px;
    line-height: 38.5px;
    letter-spacing: 4px;
  }
  .footer-bands {
    position: absolute;
    left: 0;
    bottom: 0;
    width: 861px;
    height: 31px;
  }
</style>
</head>
<body>
  <section class="card card-front">
    <h1 class="front-name">Northbrook Financial Inc.</h1>
  </section>

  <section class="card card-back">
    <h2 class="back-company">Northbrook Financial Inc<span class="dot">.</span></h2>

    <p class="person-name">Daniel Hale</p>
    <p class="person-title">Director</p>
    <div class="divider"></div>

    <ul class="contact-list">
      <li class="contact-item">
        <svg class="contact-icon" viewBox="0 0 24 24" aria-hidden="true">
          <path d="M6.6 10.8c1.4 2.8 3.8 5.1 6.6 6.6l2.2-2.2c.3-.3.7-.4 1-.2 1.1.4 2.3.6 3.6.6.6 0 1 .4 1 1V20c0 .6-.4 1-1 1C10.6 21 3 13.4 3 4c0-.6.4-1 1-1h3.5c.6 0 1 .4 1 1 0 1.3.2 2.5.6 3.6.1.3 0 .7-.2 1z"/>
          <path d="M14 3a7 7 0 0 1 7 7h-1.8A5.2 5.2 0 0 0 14 4.8zM14 6.5a3.5 3.5 0 0 1 3.5 3.5h-1.8A1.7 1.7 0 0 0 14 8.3z"/>
        </svg>
        555 010 0143
      </li>
      <li class="contact-item">
        <svg class="contact-icon" viewBox="0 0 24 24" aria-hidden="true">
          <path d="M2 6h20v13H2zM3.5 7.5v.6l8.5 5.6 8.5-5.6v-.6zm0 2.4v7.6h17V9.9l-5.6 3.7 5 3.6h-.9l-5-3.1L12 15.4l-2-1.3-5 3.1h-.9l5-3.6z"/>
        </svg>
        email@mailbox.com
      </li>
      <li class="contact-item">
        <svg class="contact-icon" viewBox="0 0 24 24" aria-hidden="true">
          <path d="M12 2a10 10 0 1 0 0 20 10 10 0 0 0 0-20zm-1 2.1V7H8.2c.7-1.6 1.7-2.6 2.8-2.9zm2 0c1.1.3 2.1 1.3 2.8 2.9H13zM7.5 4.9C7 5.5 6.6 6.2 6.2 7H4.9a8 8 0 0 1 2.6-2.1zm9 0A8 8 0 0 1 19.1 7h-1.3c-.4-.8-.8-1.5-1.3-2.1zM4 9h1.7c-.2.6-.2 1.3-.2 2H4.1c0-.7 0-1.4-.1-2zm3.8 0H11v2H7.5c0-.7.1-1.4.3-2zM13 9h3.2c.2.6.3 1.3.3 2H13zm5.3 0H20c.1.6.1 1.3.1 2h-1.6c0-.7 0-1.4-.2-2zM4.1 13h1.4c0 .7.1 1.4.2 2H4.4a8 8 0 0 1-.3-2zm3.4 0H11v2H7.8c-.2-.6-.3-1.3-.3-2zm5.5 0h3.5c0 .7-.1 1.4-.3 2H13zm5.5 0h1.6c0 .7-.1 1.4-.3 2h-1.5c.1-.6.2-1.3.2-2zM4.9 17h1.3c.4.8.8 1.5 1.3 2.1A8 8 0 0 1 4.9 17zm3.3 0H11v2.9c-1.1-.3-2.1-1.3-2.8-2.9zm4.8 0h2.8c-.7 1.6-1.7 2.6-2.8 2.9zm4.8 0h1.3a8 8 0 0 1-2.6 2.1c.5-.6.9-1.3 1.3-2.1z"/>
        </svg>
        www.yoursite.com
      </li>
    </ul>

    <address class="address">
      123 Anywhere St.<br>
      Any City, ST 12345
    </address>

    <svg class="footer-bands" viewBox="0 0 861 31" preserveAspectRatio="none" aria-hidden="true">
      <polygon points="476,0 861,0 861,31 0,31 0,20 465,20" fill="#636363"/>
      <polygon points="0,6 473,6 465,20 0,20" fill="#14365a"/>
    </svg>
  </section>
</body>
</html>
```